Business Card Design Project - Small Bar

We would like a design for a business card for our new small bar in Melbourne. It is quite the 'hipster' bar and the card would need to reflect this in its design. We do have a logo which needs to be used in the card, tho how it is incorporated is up to you! :)

OK, the Bar currently has a common 'inner city' vibe, i.e. random artwork, older 30s/40's club furniture, grafitti murals on the walls, eclectic objects etc etc Current clientele would be described as "hipster", "urban professional" etc. How to describe... they are 30, have a good job but have beards, beanies and own vinyl records. :)

The card will be used to give to professional contacts and to bands/solo artists we come across to invite them to come play at our venue, so somehow I would like it to convey the image of 'professional' and 'funky' all in one. Difficult I know.

I have asked for some advice on making this brief clearer, so check back.

Thanks all in advance. :)
Updates

Sorry all

I've now been told that it is WEST MELBOURNE 3003. Apparently we are on the border and it is referred to by either west or north Melbourne, but it is definitely West Melbourne 3003.

Things you learn hey? :)

Target Market(s)

Hipsters, urbanites, the inner city crowd

Industry/Entity Type

Artists

Requirements
Must have
Name of the bar "The Lantern & Badger"
Address - 128 Pembury St, North Melbourne, Victoria 3051
Names - Paul Redfern, Dean Horwick
mobile. 0417265930 and 0439572614
Obviously we would need separate cards?
Nice to have
• Tapwall link
Tapwall 'like' icon
Should not have
• traditional designs. I am looking for something unique and funky. with FUNK! :)

```html
<!DOCTYPE html>
<html lang="en">
<head>
<meta charset="utf-8">
<title>The Lantern &amp; Badger – Business Cards</title>
<link rel="stylesheet" href="https://fonts.googleapis.com/css2?family=Schoolbell&family=Architects+Daughter&display=swap">
<style>
  :root {
    --backdrop: #d6d3ce;
    --card-paper: #f1f1ef;
    --card-edge: #b9b9b6;
    --ink: #2a2a2a;
    --rule: #3a3a3a;
    --emblem-grey: #9a9a98;
    --emblem-ring: #c7c7c5;
    --mark-tone: #c9c9c7;
    --hand: "Schoolbell", "Architects Daughter", "Comic Sans MS", cursive;
  }
  * { box-sizing: border-box; margin: 0; padding: 0; }
  html, body { width: 1200px; height: 800px; overflow: hidden; }
  body {
    background: var(--backdrop);
    position: relative;
    font-family: var(--hand);
    color: var(--ink);
  }
  .texture-defs { position: absolute; width: 0; height: 0; }

  .card {
    position: absolute;
    width: 300px;
    height: 452px;
    overflow: hidden;
    background:
      radial-gradient(ellipse at 50% 50%, rgba(255,255,255,0.85) 0%, rgba(255,255,255,0) 70%),
      var(--card-paper);
    box-shadow: inset 0 0 40px rgba(120,120,118,0.45), 0 3px 10px rgba(0,0,0,0.28);
  }
  .card__grain {
    position: absolute;
    inset: 0;
    width: 100%;
    height: 100%;
    pointer-events: none;
  }
  .card--front { left: 150px; top: 160px; }
  .card--paul { left: 450px; top: 240px; }
  .card--dean { left: 775px; top: 150px; }

  .emblem {
    position: absolute;
    left: 56px; top: 60px;
    width: 188px; height: 188px;
    border-radius: 50%;
    background: radial-gradient(circle, var(--card-paper) 0 56%, var(--emblem-grey) 57% 94%, var(--emblem-ring) 95% 100%);
  }
  .brand {
    position: absolute;
    left: 0; right: 0; top: 272px;
    text-align: center;
    font-family: var(--hand);
    font-weight: 400;
    font-size: 30px;
    line-height: 1.2;
    color: var(--ink);
    padding: 0 30px;
  }

  .rule {
    position: absolute;
    left: 18px; right: 18px;
    height: 0;
    border-top: 1.4px solid var(--rule);
  }
  .contact, .address, .social {
    position: absolute;
    left: 22px;
    font-size: 19px;
    line-height: 1.25;
    font-weight: 400;
  }
  .contact { top: 14px; }
  .address { top: 166px; }
  .anchor-motif {
    position: absolute;
    right: 30px; top: 288px;
    width: 62px; height: 74px;
    background: var(--mark-tone);
    opacity: 0.5;
    border-radius: 6px;
  }
  .social {
    top: 390px;
    display: flex;
    align-items: center;
    gap: 8px;
  }
  .social__square {
    width: 22px; height: 22px;
    background: var(--ink);
    display: inline-block;
  }
</style>
</head>
<body>

  <svg class="texture-defs" aria-hidden="true">
    <defs>
      <filter id="paper-grunge" x="0" y="0" width="100%" height="100%">
        <feTurbulence type="fractalNoise" baseFrequency="0.035" numOctaves="5" seed="7" result="noise"/>
        <feColorMatrix in="noise" type="matrix"
          values="0 0 0 0 0.45
                  0 0 0 0 0.45
                  0 0 0 0 0.44
                  0 0 0 1.6 -0.75"/>
      </filter>
      <filter id="paper-speck" x="0" y="0" width="100%" height="100%">
        <feTurbulence type="fractalNoise" baseFrequency="0.9" numOctaves="2" seed="3" result="fine"/>
        <feColorMatrix in="fine" type="matrix"
          values="0 0 0 0 0.35
                  0 0 0 0 0.35
                  0 0 0 0 0.35
                  0 0 0 2.2 -1.35"/>
      </filter>
    </defs>
  </svg>

  <section class="card card--front" aria-label="Card front">
    <svg class="card__grain" aria-hidden="true"><rect width="100%" height="100%" filter="url(#paper-grunge)"/><rect width="100%" height="100%" filter="url(#paper-speck)"/></svg>
    <div class="emblem" role="img" aria-label="Bar mascot emblem in a grey ring"></div>
    <h1 class="brand">The Lantern &amp; Badger</h1>
  </section>

  <section class="card card--paul" aria-label="Card back, Paul Redfern">
    <svg class="card__grain" aria-hidden="true"><rect width="100%" height="100%" filter="url(#paper-grunge)"/><rect width="100%" height="100%" filter="url(#paper-speck)"/></svg>
    <p class="contact">Paul Redfern<br>0417265930</p>
    <div class="rule" style="top:72px"></div>
    <div class="rule" style="top:158px"></div>
    <p class="address">128 Pembury St<br>West Melbourne 3003<br>Victoria 3051<br>Australia</p>
    <div class="rule" style="top:272px"></div>
    <div class="anchor-motif" role="img" aria-label="Faint sketched anchor motif"></div>
    <div class="rule" style="top:376px"></div>
    <p class="social">find us on Tapwall <span class="social__square"></span></p>
  </section>

  <section class="card card--dean" aria-label="Card back, Dean Horwick">
    <svg class="card__grain" aria-hidden="true"><rect width="100%" height="100%" filter="url(#paper-grunge)"/><rect width="100%" height="100%" filter="url(#paper-speck)"/></svg>
    <p class="contact">Dean Horwick<br>0439572614</p>
    <div class="rule" style="top:72px"></div>
    <div class="rule" style="top:158px"></div>
    <p class="address">128 Pembury St<br>West Melbourne 3003<br>Victoria 3051<br>Australia</p>
    <div class="rule" style="top:272px"></div>
    <div class="anchor-motif" role="img" aria-label="Faint sketched anchor motif"></div>
    <div class="rule" style="top:376px"></div>
    <p class="social">find us on Tapwall <span class="social__square"></span></p>
  </section>

</body>
</html>
```